Design for Torvel Ginger Chewy Candy!

Hello! We are Torvel Enterprises Corp, a food manufacturer and distributor based in Los Angeles, CA. We manufacture Chips, Cookies, Juices, Dairy, and last but not least, Candies! We are launching our Ginger Chewy Candy soon and we need a great design for it!

Our Ginger Chewy Candy is a perfect mixture between sweet and spicy from the ginger itself. Torvel Ginger Chewy Candy a good relief for sore throat and nausea.

Now, other than a great design, we also welcome brand suggestions for the candy.
If you can come up with a logo for the Ginger Candy, that would be swell!

We are open to unique and out of the box design. We chose a few color schemes for the design, but feel free to step out of the box if you feel it suits the brand.

We don't have the exact size for the plastic pouch, but it should be a generic small plastic pouch size (approximately 4 oz resealable plastic pouch)

Please have fun designing the project, we can't wait to see all the great designs!

Cheers!

Target Market(s)

USA and Asian market
Age 30-70
Male and Female

Industry/Entity Type

Manufacture

Font styles to use
Serif
Sans Serif
Decorative

Colors
fff3d1
fee18a
fece3e
fbc994
fce8d3

Requirements
Must have
• Torvel Logo
• A picture of ginger (illustrations or photographs are welcome)
Nice to have
• Coating suggestions like Matte surface or SPOT UV
• Give us ideas of what the name of the chewy candy should be. Product name ideas are welcome!

```html
<!DOCTYPE html>
<html lang="en">
<head>
<meta charset="utf-8">
<title>Torvel Ginger Chewy Candy – Pouch Front</title>
<link href="https://fonts.googleapis.com/css2?family=Lobster&family=Courgette&family=EB+Garamond:wght@500;600&display=swap" rel="stylesheet">
<style>
  :root {
    --bg-light: #ece2c8;
    --bg-gold: #e6c261;
    --pouch-top: #f3dc9a;
    --pouch-mid: #ecd086;
    --pouch-bottom: #d8a93c;
    --pattern: #f7e6b4;
    --cream: #f6f0dc;
    --cream-soft: #f1e4b8;
    --brown: #3f2416;
    --brown-soft: #5c3a22;
    --gold: #e2bd54;
    --gold-deep: #b9902f;
    --window: #a8894c;
  }
  html, body {
    margin: 0;
    width: 1200px;
    height: 1200px;
    overflow: hidden;
  }
  body {
    background: linear-gradient(135deg, var(--bg-light) 30%, var(--bg-gold) 100%);
  }
  .pouch-art { display: block; width: 1200px; height: 1200px; }
  .script { font-family: "Lobster", cursive; }
  .tagline { font-family: "Courgette", cursive; fill: var(--brown); font-size: 20px; }
  .brand-name { font-family: "EB Garamond", serif; font-weight: 600; fill: var(--brown-soft); font-size: 36px; }
  .flavor { font-family: "EB Garamond", serif; font-weight: 600; fill: var(--cream); font-size: 20px; letter-spacing: 3px; }
  .net-weight { font-family: "EB Garamond", serif; font-weight: 500; fill: var(--brown); font-size: 30px; }
</style>
</head>
<body>
<svg class="pouch-art" viewBox="0 0 1200 1200" xmlns="http://www.w3.org/2000/svg">
  <defs>
    <linearGradient id="pouchFill" x1="0" y1="0" x2="0.3" y2="1">
      <stop offset="0" stop-color="var(--pouch-top)"/>
      <stop offset="0.55" stop-color="var(--pouch-mid)"/>
      <stop offset="1" stop-color="var(--pouch-bottom)"/>
    </linearGradient>
    <linearGradient id="patternFade" x1="0" y1="0" x2="0" y2="1">
      <stop offset="0" stop-color="var(--pattern)" stop-opacity="0.9"/>
      <stop offset="1" stop-color="var(--pattern)" stop-opacity="0"/>
    </linearGradient>
    <radialGradient id="photoFill" cx="0.5" cy="0.5" r="0.6">
      <stop offset="0" stop-color="#e9cf9a"/>
      <stop offset="0.6" stop-color="#e7b94c"/>
      <stop offset="1" stop-color="#f6f0dc" stop-opacity="0"/>
    </radialGradient>
    <clipPath id="pouchClip">
      <path d="M336 152 H864 V240 L856 248 L864 256 V1072 H336 V256 L344 248 L336 240 Z"/>
    </clipPath>
  </defs>

  <!-- pouch body -->
  <path class="pouch" d="M336 152 H864 V240 L856 248 L864 256 V1072 H336 V256 L344 248 L336 240 Z" fill="url(#pouchFill)"/>

  <g clip-path="url(#pouchClip)">
    <!-- top decorative pattern zone -->
    <rect x="336" y="152" width="528" height="300" fill="url(#patternFade)" role="img" aria-label="Soft flowing teardrop swirl pattern in pale gold"/>

    <!-- big cream ellipse -->
    <ellipse cx="610" cy="740" rx="250" ry="170" fill="none" stroke="var(--cream-soft)" stroke-width="10" transform="rotate(-10 610 740)"/>
    <ellipse cx="608" cy="730" rx="232" ry="160" fill="var(--cream)" transform="rotate(-10 608 730)"/>

    <!-- tagline bubble -->
    <ellipse cx="590" cy="920" rx="190" ry="62" fill="var(--cream-soft)" transform="rotate(-8 590 920)"/>
  </g>

  <!-- product photo -->
  <rect x="470" y="676" width="270" height="200" rx="40" fill="url(#photoFill)" role="img" aria-label="Photo of fresh ginger root with three golden chewy candies"/>

  <!-- title band -->
  <ellipse cx="608" cy="566" rx="218" ry="100" fill="none" stroke="var(--cream)" stroke-width="6" transform="rotate(-14 608 566)"/>
  <ellipse cx="608" cy="566" rx="206" ry="90" fill="var(--brown)" transform="rotate(-14 608 566)"/>

  <g class="title" transform="rotate(-10 610 560)">
    <text class="script" x="620" y="532" text-anchor="middle" font-size="104" fill="var(--gold)" stroke="var(--brown)" stroke-width="3" paint-order="stroke">Ginger</text>
    <text class="script" x="590" y="570" text-anchor="middle" font-size="36" fill="var(--cream)">Chewy</text>
    <text class="script" x="600" y="650" text-anchor="middle" font-size="96" fill="var(--gold)" stroke="var(--brown)" stroke-width="3" paint-order="stroke">Candy</text>
  </g>

  <!-- new tag -->
  <path d="M410 374 L486 364 V428 L452 432 L446 442 L440 433 L410 436 Z" fill="var(--brown)"/>
  <text class="script" x="448" y="414" text-anchor="middle" font-size="34" fill="var(--gold)" transform="rotate(-6 448 404)">new</text>

  <!-- brand oval -->
  <ellipse cx="600" cy="376" rx="88" ry="42" fill="var(--cream)" stroke="var(--gold-deep)" stroke-width="4"/>
  <text class="brand-name" x="600" y="388" text-anchor="middle">Torvel</text>

  <!-- tagline -->
  <g class="tagline" transform="rotate(-4 440 920)">
    <text x="440" y="904">natural sweet</text>
    <text x="440" y="928">and spicy Ginger</text>
    <text x="440" y="952">Chewy Candy</text>
  </g>

  <!-- candy windows -->
  <g class="windows" fill="var(--window)" stroke="var(--cream-soft)" stroke-width="3">
    <rect x="654" y="888" width="38" height="60" rx="8"/>
    <rect x="706" y="886" width="38" height="60" rx="8"/>
    <rect x="758" y="884" width="38" height="60" rx="8"/>
  </g>

  <!-- flavor band -->
  <path d="M440 968 H760 L752 982 L760 996 H440 L448 982 Z" fill="var(--gold-deep)" opacity="0.85"/>
  <line x1="460" y1="982" x2="498" y2="982" stroke="var(--cream)" stroke-width="1.5"/>
  <line x1="702" y1="982" x2="740" y2="982" stroke="var(--cream)" stroke-width="1.5"/>
  <text class="flavor" x="600" y="989" text-anchor="middle">ORIGINAL FLAVOR</text>

  <!-- net weight -->
  <text class="net-weight" x="600" y="1040" text-anchor="middle">Net Wt. 4oz | 113gr</text>
</svg>
</body>
</html>
```